Build a new Capability Statement for a labour support and maintenance company

Hi Everyone,
We wish to update our capability statement. Attached is a powerpoint that has the key ideas with random pictures we would like in the document. I have also attached a competitors document as a sample of the things we like. This document is being sent to our entire client base which includes Tier 1 mining companies like Vela Corran & KQS

Target Market(s)

Mining Companies

Industry/Entity Type

Mining

Colors

Designer to choose colors to be used in the design.

```html
<!DOCTYPE html>
<html lang="en">
<head>
<meta charset="utf-8">
<title>IMC Capability Statement – Company Profile &amp; Contents</title>
<link href="https://fonts.googleapis.com/css2?family=Questrial&family=Mulish:wght@700;800&display=swap" rel="stylesheet">
<style>
  :root {
    --backdrop: #a4a5a9;
    --page-dark: #545454;
    --page-darker: #3f3f41;
    --paper: #ffffff;
    --accent: #e8891e;
    --text-light: #ffffff;
    --text-soft: #e6e6e6;
    --rule: #bdbdbd;
    --sky: #9fb6cf;
    --earth: #c8734a;
    --earth-deep: #a5512d;
  }
  * { margin: 0; padding: 0; box-sizing: border-box; }
  html, body { width: 1200px; height: 900px; overflow: hidden; }
  body {
    background: var(--backdrop);
    font-family: "Questrial", "Century Gothic", sans-serif;
    color: var(--text-light);
    position: relative;
  }
  .spread {
    position: absolute;
    left: 100px; top: 93px;
    width: 1000px; height: 714px;
    display: flex;
  }
  .page { position: relative; width: 500px; height: 714px; overflow: hidden; }

  /* Left page: company profile */
  .page--profile { background: var(--page-dark); }
  .profile-title {
    position: absolute; right: 114px; top: 112px;
    font-size: 30px; letter-spacing: 1px; font-weight: 400;
  }
  .profile-tagline {
    position: absolute; right: 119px; top: 176px;
    width: 240px; text-align: right;
    font-family: "Mulish", sans-serif; font-weight: 800;
    font-size: 11.5px; line-height: 15px; text-transform: uppercase;
  }
  .profile-rule {
    position: absolute; left: 148px; top: 232px;
    width: 233px; height: 1px; background: var(--rule);
  }
  .profile-body {
    position: absolute; left: 151px; top: 252px; width: 228px;
    font-size: 9.6px; line-height: 13.4px; color: var(--text-soft);
  }
  .profile-body p { margin-bottom: 10px; }
  .profile-clients {
    position: absolute; left: 151px; top: 530px; width: 228px;
    font-family: "Mulish", sans-serif; font-weight: 700;
    font-size: 9.4px; line-height: 12.8px;
  }
  .page-tab {
    position: absolute; bottom: 3px; width: 72px; height: 80px;
    background: var(--accent);
    display: flex; align-items: center; justify-content: center; gap: 5px;
    font-size: 7px;
  }
  .page--profile .page-tab { left: 51px; }

  /* Right page: table of contents */
  .page--contents { background: var(--paper); }
  .contents-band {
    position: absolute; left: 0; top: 0; width: 284px; height: 100%;
    background: linear-gradient(90deg, var(--page-darker) 0%, var(--page-dark) 40%, #5d5d5f 100%);
  }
  .contents-photo {
    position: absolute; left: 0; top: 122px; width: 500px; height: 473px;
    background:
      linear-gradient(180deg, var(--sky) 0%, #c9d3dc 36%, var(--earth) 44%, var(--earth-deep) 100%);
  }
  .contents-shade {
    position: absolute; left: 0; top: 122px; width: 500px; height: 473px;
    background: linear-gradient(90deg, rgba(35,35,38,.92) 0%, rgba(45,45,48,.75) 35%, rgba(60,60,62,.35) 57%, rgba(0,0,0,0) 58%);
  }
  .contents-heading {
    position: absolute; left: 54px; top: 403px;
    transform: translate(-50%, -50%) rotate(-90deg);
    transform-origin: center; left: 78px;
    white-space: nowrap; font-size: 27px; letter-spacing: 1.5px;
  }
  .contents-marker {
    position: absolute; left: 58px; top: 578px; width: 29px; height: 55px;
    background: var(--accent);
  }
  .toc-item { position: absolute; left: 167px; width: 200px; }
  .toc-title {
    font-family: "Mulish", sans-serif; font-weight: 800;
    font-size: 9.5px; line-height: 13px; text-transform: uppercase;
  }
  .toc-desc { font-size: 8px; line-height: 11px; color: var(--text-soft); margin-top: 5px; }
  .toc-number {
    position: absolute; left: 345px; font-size: 34px; color: var(--text-light);
    font-weight: 400; line-height: 1;
  }
  .page--contents .page-tab { left: 370px; bottom: 5px; width: 68px; }
</style>
</head>
<body>
  <main class="spread">
    <section class="page page--profile">
      <h1 class="profile-title">COMPANY PROFILE</h1>
      <p class="profile-tagline">We believe our repeat clients are evidence ofour commitment to excellence</p>
      <div class="profile-rule"></div>
      <div class="profile-body">
        <p>Ironridge Mining and Civil Pty Ltd (IMC) have a fully mobile workforce as well as an extensive schedule of plant and equipment to support any project.</p>
        <p>We are a family owned WA business backed by a loyal team of motivated and skilled individuals who are always available to meet your needs.</p>
        <p>We understand downtime can be costly to companies which is why IMC is committed to providing cost effective and efficient solutions for your business. Project objectives are always met with outstanding client service and field excellence.</p>
        <p>Since our inception in 2011 clients who engage IMC have become confident that they will receive professional, proficient and qualified people and plant on their jobs.</p>
      </div>
      <p class="profile-clients">Some past and present clients include Vela Corran, Tarvell, Corvex Iron, Southmark Construction Pty Ltd, Halden Industries, Brookfall Mining, Marlow Mining, Kestra Mining &amp; Kestra Civil</p>
      <div class="page-tab">
        <svg width="10" height="12" viewBox="0 0 10 12" aria-hidden="true"><path d="M0 0 L10 6 L0 12 Z" fill="#3d3d3d"/></svg>
        <span>02</span>
      </div>
    </section>

    <section class="page page--contents">
      <div class="contents-band"></div>
      <div class="contents-photo" role="img" aria-label="Large excavator working on red earth at a mine site under a pale blue sky"></div>
      <div class="contents-shade"></div>
      <h2 class="contents-heading">TABLE OF CONTENT</h2>
      <div class="contents-marker"></div>

      <div class="toc-item" style="top:148px">
        <div class="toc-title">IMC Labour Support &amp;<br>Rapid Response</div>
        <div class="toc-desc">IMC is available for rapid<br>response, onsite support</div>
      </div>
      <div class="toc-number" style="top:150px">01</div>

      <div class="toc-item" style="top:356px">
        <div class="toc-title">Labour Support Projects</div>
        <div class="toc-desc">We have the quality equipment<br>and experienced operator to deliver</div>
      </div>
      <div class="toc-number" style="top:354px">02</div>

      <div class="toc-item" style="top:408px">
        <div class="toc-title">Trackline Resources</div>
        <div class="toc-desc">We have the quality equipment<br>and experienced operator to deliver</div>
      </div>
      <div class="toc-number" style="top:405px">03</div>

      <div class="toc-item" style="top:468px">
        <div class="toc-title">Equipment Hire</div>
        <div class="toc-desc">We have the quality equipment<br>and experienced operator to deliver</div>
      </div>
      <div class="toc-number" style="top:460px">04</div>

      <div class="toc-item" style="top:531px">
        <div class="toc-title">Redgum Workshop</div>
        <div class="toc-desc">We have the quality equipment<br>and experienced operator to deliver</div>
      </div>
      <div class="toc-number" style="top:524px">05</div>

      <div class="page-tab"><span>03</span></div>
    </section>
  </main>
</body>
</html>
```